International wholesale business needs a business card

We need a business card.

Company Details:
Company Name and logo
Address, Phone number, Website
Employee Details:
Name, Designation, Mobile Number & Email address

Logo file is attached.

```html
<!DOCTYPE html>
<html lang="en">
<head>
<meta charset="utf-8">
<title>Korvane Trading – Business Card</title>
<link rel="stylesheet" href="https://fonts.googleapis.com/css2?family=Playfair+Display:wght@700&family=Poppins:wght@400;500&display=swap">
<style>
  :root {
    --backdrop: #a9aeb0;
    --card: #f3f2f0;
    --brand-red: #c8262e;
    --brand-grey: #8c9298;
    --ink: #4a4d52;
    --serif: "Playfair Display", Georgia, serif;
    --sans: "Poppins", Arial, sans-serif;
  }
  * { box-sizing: border-box; margin: 0; padding: 0; }
  html, body { width: 1200px; height: 824px; overflow: hidden; }
  body {
    background: var(--backdrop);
    display: flex;
    align-items: center;
    justify-content: center;
    gap: 56px;
  }
  .card {
    position: relative;
    width: 520px;
    height: 297px;
    background: var(--card);
    border-bottom: 4px solid var(--brand-red);
    box-shadow: 0 12px 28px rgba(0,0,0,.18);
    overflow: hidden;
  }
  .card__arcs { position: absolute; inset: 0; }

  .contact {
    position: absolute;
    left: 24px;
    top: 62px;
    font-family: var(--sans);
    color: var(--ink);
    font-size: 11px;
    line-height: 1.45;
  }
  .contact__name {
    font-family: var(--serif);
    font-weight: 700;
    color: var(--brand-red);
    font-size: 15px;
    letter-spacing: .3px;
  }
  .contact__role { color: var(--brand-grey); font-size: 10.5px; margin-bottom: 6px; }
  .contact__address { margin-bottom: 6px; }
  .contact__line { display: flex; align-items: center; gap: 7px; }
  .contact__line svg { width: 10px; height: 10px; fill: var(--brand-red); flex: none; }

  .brand-vertical {
    position: absolute;
    right: 46px;
    bottom: 24px;
    transform-origin: right bottom;
    transform: rotate(-90deg) translateX(100%);
    font-family: var(--serif);
    font-weight: 700;
    color: var(--brand-red);
    line-height: 1;
    white-space: nowrap;
  }
  .brand-vertical__name { display: block; font-size: 46px; }
  .brand-vertical__sub { display: block; font-size: 15px; letter-spacing: 9px; margin-top: 6px; }

  .card--back { display: flex; align-items: center; justify-content: center; gap: 16px; }
  .brand-dot { width: 44px; height: 44px; border-radius: 50%; background: var(--brand-grey); }
  .brand-back {
    font-family: var(--serif);
    font-weight: 700;
    color: var(--brand-red);
    line-height: 1;
  }
  .brand-back__name { display: block; font-size: 42px; }
  .brand-back__sub { display: block; font-size: 14px; letter-spacing: 10px; margin-top: 6px; }
</style>
</head>
<body>

<section class="card card--front" aria-label="Card front with contact details">
  <svg class="card__arcs" viewBox="0 0 520 297" aria-hidden="true">
    <path d="M -40 -30 A 280 280 0 0 1 238 285" fill="none" stroke="var(--brand-grey)" stroke-width="32"/>
    <circle cx="-40" cy="250" r="320" fill="none" stroke="var(--brand-red)" stroke-width="26"/>
  </svg>

  <div class="contact">
    <div class="contact__name">DANIEL REYES</div>
    <div class="contact__role">President</div>
    <div class="contact__address">4120 Birchwood Road<br>Fairbanks, Alaska 39812</div>
    <div class="contact__line">
      <svg viewBox="0 0 10 10"><path d="M2 0l2 2-1 1.5c.6 1.4 1.6 2.4 3 3L7.5 5.5l2 2L8 9.5C4 9 1 6 .5 2z"/></svg>
      482-317-6054
    </div>
    <div class="contact__line">
      <svg viewBox="0 0 10 10"><path d="M2.5 0h5v10h-5zM3.5 1v7h3V1z"/></svg>
      482-731-2096
    </div>
    <div class="contact__line">
      <svg viewBox="0 0 10 10"><path d="M0 2h10v6H0zM1 3v.4l4 2.4 4-2.4V3z"/></svg>
      info@korvanetrading.com
    </div>
    <div class="contact__line">
      <svg viewBox="0 0 10 10"><circle cx="5" cy="5" r="5"/></svg>
      korvanetrading.com
    </div>
  </div>

  <div class="brand-vertical">
    <span class="brand-vertical__name">KORVANE</span>
    <span class="brand-vertical__sub">TRADING</span>
  </div>
</section>

<section class="card card--back" aria-label="Card back with company name">
  <span class="brand-dot" aria-hidden="true"></span>
  <div class="brand-back">
    <span class="brand-back__name">KORVANE</span>
    <span class="brand-back__sub">TRADING</span>
  </div>
</section>

</body>
</html>
```